Medical Billing - Professional Marketing Flier

We are needing help designing a clean and professional looking easy to read marketing flier for a medical billing practice. The text needs to be large enough to print. We are looking for a 5.5 x 8.5 design that we can edit the text as needed. I have included our logo and what we initially want it to say. Please keep in mind, we also want our logo and contact details on the flier. Let me know if you have any questions.

```html
<!DOCTYPE html>
<html lang="en">
<head>
<meta charset="utf-8">
<title>Vega Medical Billing – Flier</title>
<link href="https://fonts.googleapis.com/css2?family=Oswald:wght@400;600;700&family=Arimo:wght@400&display=swap" rel="stylesheet">
<style>
  :root {
    --ink: #0a0a0c;
    --white: #f4f4f6;
    --accent-blue: #1f9ad8;
    --pink: #cf4fa6;
    --violet: #8a45c9;
    --indigo: #5b3fd0;
    --photo-light: #c9d9ea;
    --photo-mid: #7fa6cf;
    --band-text: #161616;
    --body-text: #f0f0f2;
    --logo: #9c55cf;
  }
  * { margin: 0; padding: 0; box-sizing: border-box; }
  html, body { width: 972px; height: 1200px; overflow: hidden; background: var(--ink); }
  .flier { position: relative; width: 972px; height: 1200px; background: var(--ink); overflow: hidden; font-family: "Arimo", Arial, sans-serif; color: var(--body-text); }

  .hero { position: absolute; left: 0; top: 0; width: 972px; height: 400px; overflow: hidden; }
  .hero-photo { position: absolute; inset: 0; background: linear-gradient(135deg, #e6eef6 0%, var(--photo-light) 40%, var(--photo-mid) 75%, #4d7fb8 100%); }
  .hero-shape { position: absolute; inset: 0; }
  .hero-title { position: absolute; left: 70px; top: 64px; font-family: "Oswald", sans-serif; font-weight: 700; color: var(--white); line-height: 1; }
  .hero-kicker { font-size: 50px; letter-spacing: 1px; }
  .hero-name { font-size: 178px; letter-spacing: 2px; margin-top: -2px; line-height: 0.95; }
  .hero-line { font-size: 50px; letter-spacing: 1px; margin-top: 6px; }
  .tagline { position: absolute; left: 0; top: 348px; width: 860px; height: 38px; background: var(--white); clip-path: polygon(0 0, 100% 0, 97% 100%, 0 100%); }
  .tagline-text { position: absolute; left: 72px; top: 2px; font-family: "Oswald", sans-serif; font-weight: 600; font-size: 23px; color: var(--band-text); }

  .service { position: absolute; width: 400px; }
  .service-head { display: flex; align-items: center; gap: 14px; margin-bottom: 18px; }
  .service-icon { width: 32px; height: 30px; flex: none; }
  .service-icon.wide { width: 50px; }
  .service-title { font-family: "Oswald", sans-serif; font-weight: 600; font-size: 27px; color: var(--accent-blue); letter-spacing: 0.3px; line-height: 1; }
  .service-body { font-size: 16.5px; line-height: 19.6px; }
  .billing { left: 72px; top: 456px; }
  .aging { left: 542px; top: 456px; }
  .credentialing { left: 72px; top: 748px; }
  .contact { left: 542px; top: 748px; }

  .contact-details { position: absolute; left: 66px; top: 1030px; font-size: 19px; line-height: 25px; }
  .web-bar { position: absolute; left: 0; top: 1116px; width: 580px; height: 36px; background: linear-gradient(90deg, var(--accent-blue) 0%, #1d5f8c 40%, rgba(10,10,12,0) 100%); }
  .web-text { position: absolute; left: 64px; top: 1116px; font-family: "Oswald", sans-serif; font-weight: 600; font-size: 24px; line-height: 36px; color: var(--white); }

  .brand { position: absolute; left: 640px; top: 1080px; display: flex; align-items: center; gap: 12px; }
  .brand-dot { width: 16px; height: 16px; border-radius: 50%; background: var(--logo); }
  .brand-name { font-family: "Oswald", sans-serif; font-weight: 400; font-size: 30px; color: var(--logo); letter-spacing: 1px; }
</style>
</head>
<body>
<main class="flier">
  <header class="hero">
    <div class="hero-photo" role="img" aria-label="Photo of a stethoscope resting on medical billing statements"></div>
    <svg class="hero-shape" width="972" height="400" viewBox="0 0 972 400" aria-hidden="true">
      <defs>
        <linearGradient id="heroGrad" x1="0" y1="0" x2="1" y2="0.4">
          <stop offset="0" stop-color="var(--pink)"/>
          <stop offset="0.55" stop-color="var(--violet)"/>
          <stop offset="1" stop-color="var(--indigo)"/>
        </linearGradient>
      </defs>
      <polygon points="0,0 690,0 752,185 670,400 0,400" fill="url(#heroGrad)"/>
    </svg>
    <h1 class="hero-title">
      <div class="hero-kicker">WHY CHOOSE</div>
      <div class="hero-name">VEGA</div>
      <div class="hero-line">MEDICAL BILLING?</div>
    </h1>
    <div class="tagline"><p class="tagline-text">Medical Billing tailored to your practices needs</p></div>
  </header>

  <section class="service billing">
    <div class="service-head">
      <svg class="service-icon" viewBox="0 0 32 30" fill="none" stroke="#e8e8ea" stroke-width="1.6" aria-hidden="true">
        <rect x="3" y="2" width="22" height="26"/><path d="M7 8h14M7 12h14M7 16h14M7 20h9M25 22h4v6H8"/>
      </svg>
      <h2 class="service-title">MEDICAL BILLING</h2>
    </div>
    <p class="service-body">Would you prefer to spend time focusing on your clients and running your practice rather than trying to stay up to speed with the constantly changing medical billing rules and regulations? Let us help you by managing your medical billing and dealing with the insurance companies on your behalf! We work with you to tailor the entire medical billing process to suit your practices needs while making it as smooth and painless as possible.</p>
  </section>

  <section class="service aging">
    <div class="service-head">
      <svg class="service-icon" viewBox="0 0 32 30" fill="none" stroke="#e8e8ea" stroke-width="1.6" aria-hidden="true">
        <rect x="2" y="4" width="28" height="24" rx="3"/><path d="M2 10h28M9 1v6M23 1v6"/>
        <text x="16" y="23" font-family="Arimo, sans-serif" font-size="8" fill="#e8e8ea" stroke="none" text-anchor="middle">JAN</text>
      </svg>
      <h2 class="service-title">AGING</h2>
    </div>
    <p class="service-body">Are you leaving money on the table? Are you able to do the follow-through needed to keep your aging in check and more money flowing into your practice? Are you uncertain about how to get insurance to pay on claims that should be covered but for some reason they decided not to? We can clean up your aging, reduce the amount of time it takes for claims to pay out, and we can keep your aging to a minimum.</p>
  </section>

  <section class="service credentialing">
    <div class="service-head">
      <svg class="service-icon wide" viewBox="0 0 50 30" fill="none" stroke="#e8e8ea" stroke-width="1.6" aria-hidden="true">
        <rect x="2" y="3" width="46" height="24"/><rect x="6" y="7" width="16" height="16" rx="3"/>
        <circle cx="14" cy="13" r="3"/><path d="M9 21c1-4 9-4 10 0M26 9h18M26 14h18M26 19h18M26 23h12"/>
      </svg>
      <h2 class="service-title">CREDENTIALING</h2>
    </div>
    <p class="service-body">Are you wanting to get contracted with insurance companies but aren’t sure how to go about it? Are you wanting to expand your client base by having the option to bill insurance? Let us take the confusion out of what can seem like a daunting task! We can get you and your practitioners contracted with the insurance companies of your choice and help you navigate through the process every step of the way!</p>
  </section>

  <section class="service contact">
    <div class="service-head">
      <svg class="service-icon" viewBox="0 0 32 30" fill="none" stroke="#e8e8ea" stroke-width="1.6" aria-hidden="true">
        <rect x="14" y="1" width="16" height="10" rx="2"/><path d="M17 5h10M17 8h6"/>
        <circle cx="8" cy="9" r="4"/><path d="M1 22c0-5 14-5 14 0v2H1z"/>
        <circle cx="23" cy="18" r="3.5"/><path d="M16 29c0-5 14-5 14 0"/>
      </svg>
      <h2 class="service-title">CONTACT US</h2>
    </div>
    <p class="service-body">If any of these processes are something you would like our help with or to consult with us on, please email us or give us a call! We specialize in billing and contracting for Nutritionists and Dietitians. We would love to help you expand your business and take the pain and frustration out of billing so you can focus on your clients.</p>
  </section>

  <address class="contact-details" style="font-style:normal">
    555-014-0288<br>
    Email : admin@vegamedicalbilling.com<br>
    PO Box 418 Cedar Falls, WA 98000
  </address>

  <div class="web-bar"></div>
  <p class="web-text">WWW.VEGAMEDICALBILLING.COM</p>

  <div class="brand">
    <span class="brand-dot"></span>
    <span class="brand-name">VEGA MEDICAL BILLING</span>
  </div>
</main>
</body>
</html>
```